We need a refreshed business card. Our company is a venture capital investment firm focused on investing in medical devices. Logo is attached. please also see our website www.velmoracapital.example

Target Market(s)

investors and potential investment targets

Industry/Entity Type

medical investments

Contact Information for Business Card

logo, name, title, email, phone, website, address,

Colors
0054AA
0677BA
7BADD7
CADEEF
E8F1F8
0094D4
00A9DD
6FCCEA
C7EBF8
E9F6FB
00AB8E
00BBA5
67D7C9
C6EFE9
E9F9F6

Requirements
Must have
• fresh modern design
Nice to have
• QR code leading to our linked in page, short description of what we do “Early Stage Medical Device Investors”

```html
<!DOCTYPE html>
<html lang="en">
<head>
<meta charset="utf-8">
<title>Velmora Business Card</title>
<link href="https://fonts.googleapis.com/css2?family=Arimo:wght@400;700&family=Montserrat:wght@500;700&display=swap" rel="stylesheet">
<style>
  :root {
    --brand-blue: #0054AA;
    --card-blue: #0D57A6;
    --brand-teal: #00AB8E;
    --stage: #D6D6D6;
    --paper: #FFFFFF;
    --ink: #1A1A1A;
  }
  html, body {
    margin: 0;
    width: 1200px;
    height: 788px;
    overflow: hidden;
    background: var(--stage);
  }
  .canvas {
    position: relative;
    width: 1200px;
    height: 788px;
  }
  .card {
    position: absolute;
    top: 240px;
    width: 540px;
    height: 309px;
    border-radius: 18px;
    overflow: hidden;
    box-shadow: 0 6px 18px rgba(0,0,0,0.18);
  }
  .card--front { left: 45px; background: var(--paper); }
  .card--back { left: 615px; background: var(--card-blue); }
  .card__art {
    position: absolute;
    inset: 0;
    width: 100%;
    height: 100%;
  }
  .wordmark {
    position: absolute;
    margin: 0;
    font-family: "Arimo", Arial, sans-serif;
    font-weight: 700;
    letter-spacing: 0.5px;
  }
  .wordmark--front {
    left: 30px;
    top: 30px;
    font-size: 44px;
    color: var(--brand-blue);
  }
  .wordmark--back {
    left: 0;
    right: 0;
    top: 118px;
    text-align: center;
    font-size: 60px;
    color: var(--paper);
  }
  .person {
    position: absolute;
    left: 30px;
    top: 100px;
  }
  .person__name {
    margin: 0;
    font-family: "Montserrat", Arial, sans-serif;
    font-weight: 700;
    font-size: 22px;
    letter-spacing: 0.5px;
    color: var(--brand-teal);
    line-height: 1.1;
  }
  .person__title {
    margin: 2px 0 0;
    font-family: "Arimo", Arial, sans-serif;
    font-size: 13px;
    color: var(--ink);
  }
  .contact {
    position: absolute;
    left: 30px;
    top: 188px;
    margin: 0;
    padding: 0;
    list-style: none;
    font-family: "Arimo", Arial, sans-serif;
    font-size: 13px;
    line-height: 19px;
    color: var(--paper);
  }
  .contact__item {
    display: flex;
    align-items: center;
    gap: 7px;
  }
  .contact__icon {
    width: 12px;
    height: 12px;
    flex: none;
  }
</style>
</head>
<body>
<main class="canvas">

  <section class="card card--front" aria-label="Business card front">
    <svg class="card__art" viewBox="0 0 540 309" aria-hidden="true">
      <polygon fill="var(--card-blue)"
        points="0,172 410,150 325,70 498,168 452,88 522,0 540,0 540,309 0,309"/>
      <polyline fill="none" stroke="var(--brand-teal)" stroke-width="3" stroke-linejoin="miter"
        points="0,172 410,150 325,70 498,168 452,88 522,0"/>
    </svg>

    <p class="wordmark wordmark--front">Velmora</p>

    <div class="person">
      <h1 class="person__name">DANA WHITFIELD</h1>
      <p class="person__title">CEO/Founder</p>
    </div>

    <ul class="contact">
      <li class="contact__item">2750 Harlow Ridge Rd,</li>
      <li class="contact__item">Austin TX 78704, USA</li>
      <li class="contact__item">
        <svg class="contact__icon" viewBox="0 0 12 12" aria-hidden="true">
          <path fill="var(--brand-teal)" d="M2.5 1 L4.5 1 L5.3 3.6 L4 4.6 C4.7 6 6 7.3 7.4 8 L8.4 6.7 L11 7.5 L11 9.5 C11 10.3 10.3 11 9.5 11 C5 11 1 7 1 2.5 C1 1.7 1.7 1 2.5 1 Z"/>
        </svg>
        512-555-0148
      </li>
      <li class="contact__item">
        <svg class="contact__icon" viewBox="0 0 12 12" aria-hidden="true">
          <rect x="0.5" y="2" width="11" height="8" fill="var(--brand-teal)"/>
          <polyline points="0.8,2.4 6,6.6 11.2,2.4" fill="none" stroke="var(--card-blue)" stroke-width="1"/>
        </svg>
        info@velmoracapital.example
      </li>
      <li class="contact__item">
        <svg class="contact__icon" viewBox="0 0 12 12" aria-hidden="true">
          <circle cx="6" cy="6" r="5.5" fill="var(--brand-teal)"/>
          <path d="M0.8 6 H11.2 M6 0.6 C3.5 3.5 3.5 8.5 6 11.4 M6 0.6 C8.5 3.5 8.5 8.5 6 11.4" fill="none" stroke="var(--card-blue)" stroke-width="0.8"/>
        </svg>
        www.velmoracapital.example
      </li>
    </ul>
  </section>

  <section class="card card--back" aria-label="Business card back">
    <p class="wordmark wordmark--back">Velmora</p>
  </section>

</main>
</body>
</html>
```